Margot Vellacott Designs

- Interior design consultant
- Want a monogram/logo at the top within a circle similar to tallowmerestudio.com.au
- Want the colors, font, theme, layout to be similar to tallowmerestudio.com.au
- Monogram possibly in the gold circle/leaf thing as visible on the attached pictures, maybe a MV with a backwards "E" within a circle
- Black background, white writing
- 1 side an enlarge logo with nothing else, other side to have a small logo at top with company name, mobile and email below

Industry/Entity Type

It Company

Contact Information for Business Card

Company name: Margot Vellacott Interiors
Mobile: 0481 356 914
Email: margotvellacott@quillpost.com

Colors
000000
ffffff

```html
<!DOCTYPE html>
<html lang="en">
<head>
<meta charset="utf-8">
<title>Margot Vellacott Interiors — Business Card</title>
<link rel="stylesheet" href="https://fonts.googleapis.com/css2?family=Tinos:wght@400;700&display=swap">
<style>
  :root {
    --backdrop: #e9e6e1;
    --card-black: #0b0b0b;
    --card-sheen: #262626;
    --ink-white: #ffffff;
    --shadow: rgba(0, 0, 0, 0.28);
  }
  * { margin: 0; padding: 0; box-sizing: border-box; }
  html, body {
    width: 1200px;
    height: 885px;
    overflow: hidden;
    background: var(--backdrop);
  }
  .canvas {
    width: 1200px;
    height: 885px;
    display: flex;
    align-items: center;
    justify-content: center;
    gap: 40px;
  }
  .card {
    width: 540px;
    height: 309px;
    border-radius: 16px;
    background: radial-gradient(ellipse at 45% 40%, var(--card-sheen) 0%, var(--card-black) 70%);
    box-shadow: 0 14px 30px var(--shadow);
    color: var(--ink-white);
    font-family: "Tinos", "Times New Roman", serif;
    display: flex;
    flex-direction: column;
    align-items: center;
    justify-content: center;
  }
  .card-front { gap: 26px; }
  .brand-circle {
    width: 116px;
    height: 116px;
    border-radius: 50%;
    background: var(--card-black);
    border: 3px solid var(--ink-white);
  }
  .brand-name {
    font-weight: 700;
    font-size: 27px;
    letter-spacing: 0.2px;
  }
  .card-back { gap: 10px; }
  .contact-line {
    font-weight: 400;
    font-size: 30px;
    letter-spacing: 0.5px;
  }
</style>
</head>
<body>
  <main class="canvas">
    <section class="card card-front">
      <div class="brand-circle"></div>
      <h1 class="brand-name">Margot Vellacott Interiors</h1>
    </section>
    <section class="card card-back">
      <p class="contact-line contact-phone">0481 356 914</p>
      <p class="contact-line contact-email">margotvellacott@quillpost.com</p>
    </section>
  </main>
</body>
</html>
```